RMCCCUL re-branding website and logo

We are looking for a new webpage design and logo our current page address is www.rmccculhub.org. We want to create a new design using RMCCCUL Ridgeway and Meadowland Craftsmen Co-operative Credit Union limited and another with the purposed new name RMFC Ridgeway and Meadowland Financial Co-operative, the color scheme is purple and burnt orange. Our new logo and webpage should communicate change and growth purposed theme continuing our legacy here to server past, present and future generations. Our idea for the logo is a live shot of hands of different ages in a circle holding a tree

Target Market(s)

Everyone

Contact Information for Business Card

Company Name
Telephone number
Address
slot to enter employee info

Logo Text

(R & M) Ridgeway And Meadowland Financial Co-operative

Coding

Coded - Design and coding required

Number of Pages Required

2 page

Colors
f37122
fbed22
6b449b

Requirements
Must have
• links for social media

```html
<!DOCTYPE html>
<html lang="en">
<head>
<meta charset="utf-8">
<title>Ridgeway and Meadowland Financial Co-operative</title>
<link href="https://fonts.googleapis.com/css2?family=Oswald:wght@400;500&family=Open+Sans:wght@400;600;700&family=Poppins:wght@300;400&display=swap" rel="stylesheet">
<style>
:root{
  --purple:#6b449b;
  --orange:#f7941d;
  --burnt:#f37122;
  --slate:#8f9283;
  --grey-btn:#8a8a8a;
  --text:#555;
  --text-dark:#444;
  --section-bg:#f4f4f4;
  --white:#fff;
}
*{margin:0;padding:0;box-sizing:border-box}
html,body{width:1200px;height:1200px;overflow:hidden;background:var(--white)}
body{position:relative;font-family:"Open Sans",sans-serif;color:var(--text)}
.abs{position:absolute}

/* top bar */
.topbar{left:0;top:0;width:1200px;height:33px;background:var(--purple)}
.topbar .contact{top:0;height:33px;display:flex;align-items:center;gap:8px;color:var(--white);font-family:"Oswald",sans-serif;font-size:15px;font-weight:500;letter-spacing:.3px}
.topbar .btn{top:0;height:33px;display:flex;align-items:center;justify-content:center;color:var(--white);font-family:"Oswald",sans-serif;font-size:15px;font-weight:500}
.btn-member{left:783px;width:149px;background:var(--grey-btn)}
.btn-loan{left:932px;width:268px;background:var(--burnt);justify-content:flex-start!important;padding-left:19px}

/* header */
.header{left:0;top:33px;width:1200px;height:93px;background:var(--white)}
.brand{left:158px;top:36px;display:flex;align-items:center;gap:9px}
.brand .mark{width:14px;height:14px;background:var(--burnt)}
.brand .name{font-family:"Open Sans",sans-serif;font-weight:600;font-size:16px;color:var(--text-dark);line-height:1;white-space:nowrap}
.nav{top:37px;left:0;width:1200px;font-family:"Oswald",sans-serif;font-size:18px;color:var(--text);letter-spacing:.2px}
.nav span{position:absolute;display:flex;align-items:center;gap:5px;white-space:nowrap}
.nav .caret{width:0;height:0;border-left:6px solid transparent;border-right:6px solid transparent;border-top:6px solid #aaa}

/* hero */
.hero{left:0;top:126px;width:1200px;height:478px;background:linear-gradient(100deg,#2c4a63 0%,#8ea9bd 30%,#b6c6cf 45%,#3d3b3c 75%,#1f2a34 100%)}
.hero-card{left:134px;top:183px;width:356px;height:271px;background:rgba(235,235,235,.85)}
.hero-card h1{position:absolute;left:40px;top:58px;line-height:1;font-family:"Oswald",sans-serif;font-weight:400;font-size:46px;color:#111;letter-spacing:-1px;white-space:nowrap}
.hero-card p{position:absolute;left:40px;top:113px;width:300px;font-size:16px;line-height:19px;color:#222}
.hero-card a{position:absolute;left:41px;top:171px;width:167px;height:40px;background:var(--orange);color:var(--white);font-weight:600;font-size:16px;display:flex;align-items:center;justify-content:center;text-decoration:none}
.dots{left:80px;top:530px;display:flex;gap:4px}
.dots i{width:12px;height:12px;background:#bbb}
.dots i.on{background:transparent;border:1px solid var(--burnt)}

.rates{left:131px;top:530px;display:flex}
.rate{position:relative;width:234.5px;height:74px;color:var(--white);font-family:"Oswald",sans-serif;padding:13px 0 0 19px;overflow:hidden}
.rate h3{font-weight:500;font-size:18px;line-height:1;white-space:nowrap}
.rate .apr{font-size:17px;margin-top:10px;line-height:1}
.rate .apr small{font-size:10px}
.rate svg{position:absolute;right:0;bottom:0}
.r1{background:var(--orange)}.r2{background:var(--slate)}.r3{background:var(--purple)}.r4{background:var(--burnt)}

/* reasons */
.reasons{left:0;top:604px;width:1200px;height:596px;background:var(--section-bg)}
.reasons .photo{left:156px;top:81px;width:432px;height:520px;background:linear-gradient(160deg,#d9dfe3 0%,#c7c0b6 40%,#3a3a3a 75%,#5d8d7a 100%)}
.reasons h2{left:642px;top:72px;font-family:"Poppins",sans-serif;font-weight:400;font-size:27px;color:var(--text);white-space:nowrap}
.reasons .intro{left:642px;top:124px;width:412px;font-size:11px;line-height:17.6px}
.item{left:642px;width:420px}
.item .tick{position:absolute;left:0;top:0}
.item h4{position:absolute;left:48px;top:2px;font-size:16px;font-weight:600;color:var(--text-dark);white-space:nowrap}
.item p{position:absolute;left:48px;top:36px;width:360px;font-size:11px;line-height:17.6px}
</style>
</head>
<body>

<div class="abs topbar">
  <div class="abs contact" style="left:512px">
    <svg width="14" height="14" viewBox="0 0 24 24"><path fill="#fff" d="M6.6 10.8a15 15 0 0 0 6.6 6.6l2.2-2.2c.3-.3.7-.4 1-.2 1.1.4 2.3.6 3.6.6.6 0 1 .4 1 1V20c0 .6-.4 1-1 1A17 17 0 0 1 3 4c0-.6.4-1 1-1h3.5c.6 0 1 .4 1 1 0 1.3.2 2.5.6 3.6.1.3 0 .7-.2 1z"/></svg>
    (555) 410-2286
  </div>
  <div class="abs contact" style="left:652px">
    <svg width="15" height="14" viewBox="0 0 24 22"><path fill="#fff" d="M6 0h12v6H6zM2 7h20a2 2 0 0 1 2 2v8h-5v5H5v-5H0V9a2 2 0 0 1 2-2zm5 8v5h10v-5z"/></svg>
    (555) 410-7734
  </div>
  <div class="abs btn btn-member">BECOME A MEMBER</div>
  <div class="abs btn btn-loan">APPLY FOR LOAN</div>
</div>

<header class="abs header">
  <div class="abs brand"><span class="mark"></span><span class="name">Ridgeway and Meadowland</span></div>
  <nav class="abs nav">
    <span style="left:448px">MY CREDIT UNION <i class="caret"></i></span>
    <span style="left:608px">PRODUCTS &amp; SERVICES <i class="caret"></i></span>
    <span style="left:800px">TOOLS &amp; BENEFITS <i class="caret"></i></span>
    <span style="left:962px">CONTACT US</span>
  </nav>
</header>

<section class="abs hero" role="img" aria-label="Photo of a smiling woman in a car holding up her new car keys"></section>
<div class="abs hero-card">
  <h1>Consumer Loans</h1>
  <p>Our RMFC simplify money management and help you save.</p>
  <a href="#">Learn more</a>
</div>
<div class="abs dots"><i class="on"></i><i></i><i></i></div>

<div class="abs rates">
  <div class="rate r1"><h3>CONSUMER LOANS</h3><div class="apr">9.00%<small>APR*</small></div>
    <svg width="56" height="48"><path d="M56 0V48H0Z" fill="#fff"/><path d="M33 38h16M41 30v16" stroke="#f7941d" stroke-width="2.5"/></svg></div>
  <div class="rate r2"><h3>USED AUTO/MOTORCYCLE</h3><div class="apr">11.75% <small>APR*</small></div>
    <svg width="56" height="48"><path d="M56 0V48H0Z" fill="#fff"/><path d="M33 38h16M41 30v16" stroke="#8f9283" stroke-width="2.5"/></svg></div>
  <div class="rate r3"><h3>NEW AUTO/MOTORCYCLE</h3><div class="apr">9.00%<small>APR*</small></div>
    <svg width="56" height="48"><path d="M56 0V48H0Z" fill="#fff"/><path d="M33 38h16M41 30v16" stroke="#6b449b" stroke-width="2.5"/></svg></div>
  <div class="rate r4"><h3>MORTGAGES</h3><div class="apr">8.25% <small>APR*</small></div>
    <svg width="56" height="48"><path d="M56 0V48H0Z" fill="#fff"/><path d="M33 38h16M41 30v16" stroke="#f37122" stroke-width="2.5"/></svg></div>
</div>

<section class="abs reasons">
  <div class="abs photo" role="img" aria-label="Photo of a young couple receiving car keys at a dealership"></div>
  <h2 class="abs">Reason to Choose us</h2>
  <p class="abs intro">Nam libero tempore, cum soluta nobis est eligendi optio cumque nihil impedit quo minus id quod maxime placeat facere possimus, omnis voluptas assumenda est, omnis dolor repellendus. Temporibus autem quibusdam et aut officiis debitis aut rerum necessitatibus saepe eveniet ut et voluptates repudiandae sint et molestiae non recusandae. Itaque earum rerum hic t</p>

  <div class="abs item" style="top:238px">
    <svg class="tick" width="31" height="31" viewBox="0 0 31 31"><circle cx="15.5" cy="15.5" r="15.5" fill="#f37122"/><circle cx="15.5" cy="15.5" r="11" fill="none" stroke="#fff" stroke-width="2"/><path d="M10 15.5l4 4 8-9" fill="none" stroke="#fff" stroke-width="3" stroke-linecap="round"/></svg>
    <h4>Easy Temporibus autosa</h4>
    <p>Cum sociis natoque penatibus et nis dis parturgnis dis parturient montes, nascetur ridiculus mus.</p>
  </div>
  <div class="abs item" style="top:342px">
    <svg class="tick" width="31" height="31" viewBox="0 0 31 31"><circle cx="15.5" cy="15.5" r="15.5" fill="#f37122"/><circle cx="15.5" cy="15.5" r="11" fill="none" stroke="#fff" stroke-width="2"/><path d="M10 15.5l4 4 8-9" fill="none" stroke="#fff" stroke-width="3" stroke-linecap="round"/></svg>
    <h4>Easy Temporibus autosa</h4>
    <p>Cum sociis natoque penatibus et nis dis parturgnis dis parturient montes, nascetur ridiculus mus.</p>
  </div>
  <div class="abs item" style="top:438px">
    <svg class="tick" width="31" height="31" viewBox="0 0 31 31"><circle cx="15.5" cy="15.5" r="15.5" fill="#f37122"/><circle cx="15.5" cy="15.5" r="11" fill="none" stroke="#fff" stroke-width="2"/><path d="M10 15.5l4 4 8-9" fill="none" stroke="#fff" stroke-width="3" stroke-linecap="round"/></svg>
    <h4>Easy Temporibus autosa</h4>
    <p>Cum sociis natoque penatibus et nis dis parturgnis dis parturient montes, nascetur ridiculus mus.</p>
  </div>
  <div class="abs item" style="top:542px">
    <svg class="tick" width="31" height="31" viewBox="0 0 31 31"><circle cx="15.5" cy="15.5" r="15.5" fill="#f37122"/><circle cx="15.5" cy="15.5" r="11" fill="none" stroke="#fff" stroke-width="2"/><path d="M10 15.5l4 4 8-9" fill="none" stroke="#fff" stroke-width="3" stroke-linecap="round"/></svg>
    <h4>Easy Temporibus autosa</h4>
    <p>Cum sociis natoque penatibus et nis dis parturgnis dis parturient montes, nascetur ridiculus mus.</p>
  </div>
</section>

</body>
</html>
```